Building company business card

Design and print business cards for BREVOTA PTY LTD.
A residantial homes building company.
Pixel Forge already designed the company Logo.

```html
<!DOCTYPE html>
<html lang="en">
<head>
<meta charset="utf-8">
<title>BREVOTA PTY LTD – Business Card</title>
<link href="https://fonts.googleapis.com/css2?family=Montserrat:wght@500;700;800&family=Roboto:wght@400&display=swap" rel="stylesheet">
<style>
  :root {
    --navy: #232a6b;
    --gold: #c99a3c;
    --ink: #2b2b2b;
    --card: #ffffff;
    --backdrop: #e4e3e0;
  }
  * { box-sizing: border-box; margin: 0; padding: 0; }
  html, body { width: 1200px; height: 801px; overflow: hidden; }
  body {
    background: var(--backdrop);
    display: flex;
    align-items: center;
    justify-content: center;
    gap: 48px;
    font-family: "Roboto", Arial, sans-serif;
  }
  .card {
    position: relative;
    width: 520px;
    height: 318px;
    background: var(--card);
    border-radius: 18px;
    border: 2px solid var(--navy);
    box-shadow: 0 10px 28px rgba(0,0,0,0.14);
  }
  .company {
    position: absolute; left: 36px; top: 38px;
    font-family: "Montserrat", Arial, sans-serif;
    font-weight: 700; font-size: 17px; letter-spacing: 0.5px;
    color: var(--navy);
  }
  .registration {
    position: absolute; right: 34px; top: 34px;
    text-align: right; font-size: 13px; line-height: 1.35; color: var(--ink);
  }
  .brand-mark {
    display: flex; align-items: center; gap: 10px;
    font-family: "Montserrat", Arial, sans-serif;
    font-weight: 800; color: var(--navy); letter-spacing: 1px;
  }
  .brand-square { background: var(--gold); flex: none; }
  .card-front .brand-mark {
    position: absolute; left: 180px; top: 82px; font-size: 38px;
  }
  .card-front .brand-square { width: 26px; height: 26px; }
  .holder {
    position: absolute; left: 110px; top: 150px; width: 340px; text-align: right;
  }
  .holder-name {
    font-family: "Montserrat", Arial, sans-serif;
    font-weight: 700; font-size: 22px; color: var(--navy); letter-spacing: 0.3px;
  }
  .holder-role { font-size: 14px; color: var(--ink); margin-top: 2px; }
  .divider {
    position: absolute; left: 36px; right: 34px; top: 222px;
    height: 1px; background: var(--navy);
  }
  .contacts {
    position: absolute; left: 36px; top: 234px;
    list-style: none; font-size: 14px; color: var(--ink); line-height: 1.6;
  }
  .contacts li { display: flex; align-items: center; gap: 9px; }
  .contacts svg { width: 12px; height: 14px; flex: none; }
  .postal {
    position: absolute; right: 34px; top: 238px;
    text-align: right; font-size: 14px; line-height: 1.45; color: var(--ink);
  }
  .card-back { display: flex; align-items: center; justify-content: center; }
  .card-back .brand-mark { font-size: 58px; gap: 16px; }
  .card-back .brand-square { width: 40px; height: 40px; }
</style>
</head>
<body>
  <section class="card card-front" aria-label="Business card front">
    <div class="company">BREVOTA PTY LTD</div>
    <div class="registration">ABN- 48 210 935 602<br>CDB-U 51804</div>
    <div class="brand-mark"><span class="brand-square"></span>BREVOTA</div>
    <div class="holder">
      <div class="holder-name">MARCUS (Mark) DELANEY</div>
      <div class="holder-role">Director</div>
    </div>
    <div class="divider"></div>
    <ul class="contacts">
      <li>
        <svg viewBox="0 0 12 14" aria-hidden="true"><rect x="2" y="0.8" width="8" height="12.4" rx="1.5" fill="none" stroke="var(--navy)" stroke-width="1.4"/><line x1="5" y1="11" x2="7" y2="11" stroke="var(--navy)" stroke-width="1.2"/></svg>
        0412 555 318 &amp; 0433 555 742
      </li>
      <li>
        <svg viewBox="0 0 12 14" aria-hidden="true"><rect x="0.5" y="3" width="11" height="8" fill="var(--navy)"/><polyline points="0.5,3 6,7.5 11.5,3" fill="none" stroke="#fff" stroke-width="1"/></svg>
        mdl@brevota-pl.co
      </li>
    </ul>
    <div class="postal">PO Box 482<br>Ashmere North Vic 3199</div>
  </section>

  <section class="card card-back" aria-label="Business card back">
    <div class="brand-mark"><span class="brand-square"></span>BREVOTA</div>
  </section>
</body>
</html>
```